Environmentally conscious Waste Management Company requires business card

We Require a Business card for our environmentally conscious waste management company . The business card should have a very clean design. be double sided and incorporate our logo..
The card will need o have 9 lines for the contact details - that are
Name
Title
Business
Address Line 1
Address Line 2
Address Line 3
Phone
Mobile
Email

Industry/Entity Type

Waste Management

Other font styles liked:
• Helvetica or similar

```html
<!DOCTYPE html>
<html lang="en">
<head>
<meta charset="utf-8">
<title>Brightway Recycling – Business Card</title>
<link rel="stylesheet" href="https://fonts.googleapis.com/css2?family=Open+Sans:wght@400;600&display=swap">
<style>
  :root {
    --stage: #e9ebe8;
    --green-deep: #0f5a22;
    --green-mid: #2a8f3a;
    --green-bright: #48b24f;
    --green-soft: rgba(120, 210, 120, 0.18);
    --white: #ffffff;
    --ink-light: #eaf6ea;
    --brand-ink: #1f6e2c;
    --shadow: rgba(0, 0, 0, 0.18);
  }
  * { margin: 0; padding: 0; box-sizing: border-box; }
  html, body {
    width: 1200px;
    height: 784px;
    overflow: hidden;
    background: var(--stage);
    font-family: "Open Sans", Arial, sans-serif;
  }
  .stage {
    width: 1200px;
    height: 784px;
    display: flex;
    align-items: center;
    justify-content: center;
    gap: 40px;
  }
  .card {
    position: relative;
    width: 540px;
    height: 308px;
    border-radius: 4px;
    overflow: hidden;
    box-shadow: 0 10px 24px var(--shadow);
  }

  /* Contact side */
  .card--contact { background: var(--green-deep); color: var(--ink-light); }
  .card__backdrop {
    position: absolute;
    inset: 0;
    background:
      radial-gradient(ellipse at 18% 45%, var(--green-bright) 0%, rgba(72,178,79,0) 60%),
      linear-gradient(115deg, var(--green-mid) 0%, var(--green-deep) 75%);
  }
  .card__band {
    position: absolute;
    left: 0; right: 0;
    top: 56px; height: 140px;
    background: var(--green-soft);
  }
  .card__rule {
    position: absolute;
    left: 0; right: 0;
    top: 228px; height: 1px;
    background: rgba(255, 255, 255, 0.28);
  }
  .holder {
    position: absolute;
    left: 140px;
    top: 112px;
    width: 120px;
    text-align: right;
  }
  .holder__name { font-size: 15px; font-weight: 600; color: var(--white); line-height: 1.2; white-space: nowrap; }
  .holder__title { font-size: 11px; font-weight: 400; line-height: 1.3; }
  .divider {
    position: absolute;
    left: 274px;
    top: 72px;
    width: 1px;
    height: 112px;
    background: rgba(255, 255, 255, 0.6);
  }
  .details {
    position: absolute;
    left: 286px;
    top: 64px;
    list-style: none;
    font-size: 11.5px;
    line-height: 14.4px;
    white-space: nowrap;
  }
  .details li { display: flex; align-items: center; }
  .details__icon { width: 16px; height: 11px; flex: none; margin-right: 3px; fill: var(--white); }
  .details__indent { padding-left: 19px; }
  .details__company { padding-left: 4px; }

  /* Brand side */
  .card--brand { background: var(--white); }
  .brand {
    position: absolute;
    inset: 0;
    display: flex;
    align-items: center;
    justify-content: center;
  }
  .brand__name {
    font-size: 34px;
    font-weight: 400;
    color: var(--brand-ink);
    white-space: nowrap;
  }
</style>
</head>
<body>
<main class="stage">

  <section class="card card--contact">
    <div class="card__backdrop" role="img" aria-label="Green background with a pattern of soft overlapping circles"></div>
    <div class="card__band"></div>
    <div class="card__rule"></div>

    <div class="holder">
      <p class="holder__name">Mara Lindqvist</p>
      <p class="holder__title">manager</p>
    </div>

    <div class="divider"></div>

    <ul class="details">
      <li class="details__company">Brightway Recycling, LLC</li>
      <li>
        <svg class="details__icon" viewBox="0 0 16 11" aria-hidden="true"><path d="M8 0 L15 6 H13 V11 H9.5 V7.5 H6.5 V11 H3 V6 H1 Z"/></svg>
        Address Line 1
      </li>
      <li class="details__indent">Address Line 2</li>
      <li class="details__indent">Address Line 3</li>
      <li>
        <svg class="details__icon" viewBox="0 0 16 11" aria-hidden="true"><path d="M3 0.5 C4 0 5 0.3 5.5 1.5 L6 3 C6.2 3.8 5.8 4.2 5.2 4.6 C5.8 6 7 7.2 8.4 7.8 C8.8 7.2 9.2 6.8 10 7 L11.5 7.5 C12.7 8 13 9 12.5 10 C11 11.5 8 11 5 8 C2 5 1.5 2 3 0.5 Z"/></svg>
        1402 318 776
      </li>
      <li>
        <svg class="details__icon" viewBox="0 0 16 11" aria-hidden="true"><path d="M4 0 H10 A1 1 0 0 1 11 1 V10 A1 1 0 0 1 10 11 H4 A1 1 0 0 1 3 10 V1 A1 1 0 0 1 4 0 Z M4.3 1.5 V8.5 H9.7 V1.5 Z"/></svg>
        3720 915 483
      </li>
      <li>
        <svg class="details__icon" viewBox="0 0 16 11" aria-hidden="true"><path d="M1 1 H14 V10 H1 Z M2 2 L7.5 6.5 L13 2 Z"/></svg>
        hello@brightwayrecycling.com
      </li>
    </ul>
  </section>

  <section class="card card--brand">
    <div class="brand">
      <span class="brand__name">Brightway Recycling</span>
    </div>
  </section>

</main>
</body>
</html>
```